Industrial Company needing new business cards

We are a newly branded Industrial trade company. We specialise in Electrical, Mechanical and Air-conditioning.

I would like to see designs single sided. Focusing on the color scheme white/red/black and possibly gray. Possibly make it a black card with white writting... but open to all designs.

I would like the design to be professional, sleek and to the point.

Industry/Entity Type

Business

Contact Information for Business Card

Tom Harwick
Managing Director / Electrician
tomwork@velnet.com.au
47 Garnet Road, Rutherford NSW 2320
Mobile: 0427115830
www.harwickindustrialgroup.com.au

Requirements
Must have
• Must be able to be sent in a manner that i can change the details for each employee.
• Our logo
Nice to have
• Would like it to somehow have " incorporating Talvo Group Pty Ltd" as this is the company we have taken over.
Should not have
• No yellow!!!
• must not simply place "talvo group" randomly on the business card. refer nice to have.

```html
<!DOCTYPE html>
<html lang="en">
<head>
<meta charset="utf-8">
<title>Harwick Industrial Group – Business Card</title>
<link href="https://fonts.googleapis.com/css2?family=Exo+2:wght@400;600&family=Ubuntu:wght@400&display=swap" rel="stylesheet">
<style>
  :root {
    --bg: #3b3b3b;
    --red: #dc0012;
    --black: #050505;
    --white: #f7f7f7;
    --ink: #222222;
    --grey: #6a6a6a;
  }
  * { margin: 0; padding: 0; box-sizing: border-box; }
  html, body { width: 1200px; height: 750px; overflow: hidden; background: var(--bg); }
  .canvas { position: relative; width: 1200px; height: 750px; }

  .card { position: absolute; top: 228px; width: 462px; height: 262px; overflow: hidden; }
  .card--front { left: 124px; background: var(--white); }
  .card--back { left: 618px; background: var(--red); }

  .front-panel { position: absolute; inset: 0; }

  .holder { position: absolute; left: 0; width: 210px; top: 202px; text-align: center; font-family: "Exo 2", sans-serif; }
  .holder__name { color: var(--red); font-size: 16px; font-weight: 600; line-height: 20px; }
  .holder__role { color: var(--white); font-size: 12px; font-weight: 400; line-height: 18px; }

  .brand { position: absolute; left: 226px; top: 52px; width: 210px; font-family: "Exo 2", sans-serif; }
  .brand__row { display: flex; align-items: center; gap: 8px; }
  .brand__mark { width: 14px; height: 14px; background: var(--red); flex: none; }
  .brand__name { color: var(--black); font-size: 15px; font-weight: 600; line-height: 17px; text-transform: uppercase; letter-spacing: 0.3px; }
  .brand__tagline { margin-top: 7px; color: var(--grey); font-size: 6.4px; font-weight: 600; letter-spacing: 0.1px; text-transform: uppercase; white-space: nowrap; }

  .contacts { position: absolute; right: 30px; top: 189px; list-style: none; font-family: "Ubuntu", sans-serif; font-size: 11px; color: var(--ink); }
  .contacts li { display: flex; justify-content: flex-end; align-items: center; gap: 6px; height: 17.5px; }
  .contacts svg { width: 11px; height: 11px; flex: none; }

  .back-brand { position: absolute; left: 0; right: 0; top: 112px; display: flex; justify-content: center; align-items: center; gap: 10px; font-family: "Exo 2", sans-serif; }
  .back-brand__mark { width: 16px; height: 16px; background: var(--white); }
  .back-brand__name { color: var(--white); font-size: 20px; font-weight: 600; text-transform: uppercase; letter-spacing: 1px; }
  .back-url { position: absolute; left: 0; right: 0; top: 214px; text-align: center; color: var(--white); font-family: "Ubuntu", sans-serif; font-style: italic; font-size: 11px; letter-spacing: 4.4px; }
</style>
</head>
<body>
<main class="canvas">
  <section class="card card--front">
    <svg class="front-panel" viewBox="0 0 462 262" aria-hidden="true">
      <polygon points="0,0 225,262 0,262" fill="var(--black)"/>
      <polygon points="0,0 6,0 232,262 225,262" fill="var(--red)"/>
    </svg>

    <div class="holder">
      <p class="holder__name">Tom Harwick</p>
      <p class="holder__role">Managing Director / Electrician</p>
    </div>

    <div class="brand">
      <div class="brand__row">
        <span class="brand__mark"></span>
        <span class="brand__name">Harwick Industrial Group</span>
      </div>
      <p class="brand__tagline">Electrical - Mechanical - Airconditioning</p>
    </div>

    <ul class="contacts">
      <li>0427115830
        <svg viewBox="0 0 12 12"><rect x="3" y="0.8" width="6" height="10.4" rx="1" fill="none" stroke="var(--red)" stroke-width="1.4"/><rect x="4.5" y="8.6" width="3" height="1" fill="var(--red)"/></svg>
      </li>
      <li>tomwork@velnet.com.au
        <svg viewBox="0 0 12 12"><rect x="0.5" y="2.5" width="11" height="7.5" fill="var(--red)"/><polyline points="0.8,2.8 6,7 11.2,2.8" fill="none" stroke="var(--white)" stroke-width="1"/></svg>
      </li>
      <li>harwickindustrialgroup.com.au
        <svg viewBox="0 0 12 12"><circle cx="6" cy="6" r="5.5" fill="var(--red)"/><ellipse cx="6" cy="6" rx="2.3" ry="5.2" fill="none" stroke="var(--white)" stroke-width="0.8"/><line x1="0.8" y1="6" x2="11.2" y2="6" stroke="var(--white)" stroke-width="0.8"/></svg>
      </li>
    </ul>
  </section>

  <section class="card card--back">
    <div class="back-brand">
      <span class="back-brand__mark"></span>
      <span class="back-brand__name">Harwick Industrial Group</span>
    </div>
    <p class="back-url">www.harwickindustrialgroup.com.au</p>
  </section>
</main>
</body>
</html>
```